Surviving Domestic Violence Flyer

I need a flyer that "POPS" to attract participants for my research project. I have added the important information on my draft flyer.

```html
<!DOCTYPE html>
<html lang="en">
<head>
<meta charset="utf-8">
<title>Survivor Resources Study – Request for Participants</title>
<link href="https://fonts.googleapis.com/css2?family=Roboto:wght@900&family=Oswald:wght@500&family=Roboto+Condensed:wght@700&display=swap" rel="stylesheet">
<style>
  :root{
    --ink:#000000;
    --paper:#ffffff;
    --gold:#e6b877;
    --alert:#e3232c;
    --photo-dark:#1c0f0e;
    --photo-mid:#4a2220;
    --photo-skin:#b98670;
  }
  *{margin:0;padding:0;box-sizing:border-box}
  html,body{width:926px;height:1200px;overflow:hidden;background:var(--paper)}
  .flyer{position:relative;width:926px;height:1200px;background:var(--ink);overflow:hidden;
    font-family:"Roboto Condensed","Arial Narrow",sans-serif;color:var(--paper)}
  .hero-photo{position:absolute;left:0;top:0;width:926px;height:600px;
    background:
      radial-gradient(ellipse 260px 330px at 470px 330px,var(--photo-skin) 0%,rgba(150,95,80,.55) 45%,rgba(0,0,0,0) 80%),
      linear-gradient(90deg,var(--photo-dark) 0%,var(--photo-mid) 55%,#3a1a19 100%)}
  .headline{position:absolute;left:48px;top:44px;font-family:"Roboto",Arial,sans-serif;font-weight:900;
    font-size:80px;line-height:86px;letter-spacing:-1px;color:var(--paper)}
  .study-title{position:absolute;right:36px;top:58px;text-align:right;font-family:"Oswald",sans-serif;
    font-weight:500;font-size:48px;line-height:85px;color:var(--gold);text-transform:uppercase}
  .compensation{position:absolute;left:48px;top:518px;font-size:16px;line-height:20px;color:var(--paper)}
  .divider{position:absolute;left:0;top:560px;width:926px;height:60px}
  .questions{position:absolute;left:0;top:600px;width:926px;text-align:center;font-size:23px;line-height:39px}
  .questions .highlight{color:var(--alert)}
  .details{position:absolute;left:48px;top:842px;width:520px;font-size:18.5px;line-height:23px}
  .details p+p{margin-top:10px}
  .details .link{color:var(--alert)}
  .credentials{position:absolute;left:572px;top:836px;width:330px;font-size:16px;line-height:22px}
  .credentials p{margin-bottom:8px}
  .credentials .label{color:var(--alert);text-transform:uppercase}
  .tear-tabs{position:absolute;left:0;top:1027px;width:926px;height:173px;background:var(--paper);
    display:flex;border-top:1px solid #999}
  .tab{flex:1;border-right:1px solid #888;display:flex;justify-content:center;align-items:center;gap:2px}
  .tab:last-child{border-right:none}
  .tab span{writing-mode:vertical-rl;transform:rotate(180deg);white-space:nowrap}
  .tab .tab-label{color:var(--ink);font-size:12px}
  .tab .tab-phone{color:var(--alert);font-size:17px}
</style>
</head>
<body>
<main class="flyer">
  <div class="hero-photo" role="img" aria-label="Photograph of a woman seen from behind in profile, with visible bruises and scratches on her bare shoulder and back"></div>

  <h1 class="headline">Request<br>for Study<br>Participants</h1>

  <h2 class="study-title">Efficiency<br>of Resources<br>Available<br>to Survivors<br>of Intimate<br>Partner Abuse</h2>

  <p class="compensation">Participants will be<br>compensated for their time</p>

  <svg class="divider" viewBox="0 0 926 60" preserveAspectRatio="none" aria-hidden="true">
    <path d="M0 40 Q463 -10 926 40 L926 60 L0 60 Z" fill="var(--ink)"/>
    <path d="M0 40 Q463 -10 926 40" fill="none" stroke="var(--gold)" stroke-width="3"/>
  </svg>

  <div class="questions">
    <p>Are you eighteen years of age older?</p>
    <p class="highlight">Have you been a victim of domestic violence?</p>
    <p>Have you sought assistance with abuse in the last 12 months?</p>
    <p class="highlight">Are you still in contact with a person who abused you?</p>
    <p style="line-height:30px;margin-top:4px">Are you willing and open to discussing your experience with<br>abuse and your attempts to access services or resources?</p>
  </div>

  <div class="details">
    <p>If you answered yes to all of these questions, you may be eligible to participate in a study to better understand the resources needed and services expected for survivors of domestic violence.</p>
    <p>Please contact Dana Whitlock at <span class="link">1(555)014-2290</span> or via e-mail <span class="link">survivorvoicesstudy@example.org</span> for additional information.</p>
  </div>

  <div class="credentials">
    <p><span class="label">Principal Investigator:</span> Dana Whitlock</p>
    <p><span class="label">Institutional Affiliation:</span> Lakeshore State University, Dept. of Criminology, Law and Justice</p>
    <p><span class="label">Contact Address:</span> Post Office Box 100245, Chicago, IL, 60601</p>
  </div>

  <div class="tear-tabs">
    <div class="tab"><span class="tab-label">Survivor Resources Study</span><span class="tab-phone">1(555)014-2290</span></div>
    <div class="tab"><span class="tab-label">Survivor Resources Study</span><span class="tab-phone">1(555)014-2290</span></div>
    <div class="tab"><span class="tab-label">Survivor Resources Study</span><span class="tab-phone">1(555)014-2290</span></div>
    <div class="tab"><span class="tab-label">Survivor Resources Study</span><span class="tab-phone">1(555)014-2290</span></div>
    <div class="tab"><span class="tab-label">Survivor Resources Study</span><span class="tab-phone">1(555)014-2290</span></div>
    <div class="tab"><span class="tab-label">Survivor Resources Study</span><span class="tab-phone">1(555)014-2290</span></div>
    <div class="tab"><span class="tab-label">Survivor Resources Study</span><span class="tab-phone">1(555)014-2290</span></div>
    <div class="tab"><span class="tab-label">Survivor Resources Study</span><span class="tab-phone">1(555)014-2290</span></div>
    <div class="tab"><span class="tab-label">Survivor Resources Study</span><span class="tab-phone">1(555)014-2290</span></div>
    <div class="tab"><span class="tab-label">Survivor Resources Study</span><span class="tab-phone">1(555)014-2290</span></div>
    <div class="tab"><span class="tab-label">Survivor Resources Study</span><span class="tab-phone">1(555)014-2290</span></div>
    <div class="tab"><span class="tab-label">Survivor Resources Study</span><span class="tab-phone">1(555)014-2290</span></div>
    <div class="tab"><span class="tab-label">Survivor Resources Study</span><span class="tab-phone">1(555)014-2290</span></div>
    <div class="tab"><span class="tab-label">Survivor Resources Study</span><span class="tab-phone">1(555)014-2290</span></div>
  </div>
</main>
</body>
</html>
```